Hurricane Damage Public Adjuster Billboard

I have created several projects with you and have several great designs. I need to format them into a Billboard for upcoming Hurricane Season. Need done in a month. Im also in process of getting an eye catching and easy to remember 800# Vanity phone number like Call 800-Stormfix or 800- Need Help? My included past Sketch Guild projects will give you an idea of what colors, schemes, and designs I gravitate towards. 3 past Design projects were 1) 2 Logos where I picked the 1st place and the 2nd place and 2) Index Card where I picked the winner as the Index Card and the 2nd place as a Post Card. Point is, I will pick and pay for 2 winners if they're good. This should help to sweeten the pot. Also, please look at my website for ideas that I like:

www.TheClaimWardenGroup.com
I want people to feel that I am the best and highest. Level.

I've been getting a lot of quick half effort designs basically cut & pasting my previous projects. Please don't rush and take your time to be creative. A an example, my Biggest Competitor is Crestline Public Adjusting. Their colors are Black and Gold while mine are Blue, White, and Black with a highlight of Orange if possible. I JUST imported a picture of their BillBoard. I need mine better and BLOW AWAY THEIRS. Terms like "Don't be Victimized Twice ?, Don't let the Hurricane Ruin your Life?". "Get Fairly Paid & Move On" "Our Clients Claims are VIP?
Updates

I'm getting a lot of quick half effort ones. I'd rather you take your time and really put some thoughts and effort into it. My Biggest Competitor is Crestline Public Adjusting. They have black & gold colors, while I have Blue, Black, and white.

It needs to blow theirs away. I have imported their Billboard for comparative purposes.

Guy's,
I'll make it easier for you in what I'm looking for. Please look at the Crestline Billboard picture attached.

1) Put my "Blue Shield" to the left, replacing their logo
2) change color patterns from their (Black, Gold, White) to my color schemes of (Black, Blue, White)
3) I want to see my name where their is:

THE
Claim Warden Group
EXPERT & LOCAL Public Adjusters
"FOR THE POLICYHOLDER!!"

4) to the right, add the A+Rated logo and QTR+ Accredited logo, 5 Star Zentrio Rated logo, 5 Start BLOCKLINK Highly Rated logo, etc..

5) the right side is where you can be creative as I will not have a picture of me there.

"20+ Years of Experience, Recovering Millions for our VIP Clients"

"Your Best, Locally-Based Private Adjuster & Advocate'
"FOR THE POLICYHOLDER!!"

"Don't be victimized Twice!!"

"Don't let the Hurricane Ruin Your Life!!"

This should really help. Also, refer to my website, maybe a couple testimonial fillers?

Thanks all,

marvin@TheClaimWardenGroup.com

Just imported a few awards that would look great to the right side with all the other 5 Star Ratings and accolades.
This right section could be titled like zmy Website:

5 Star Reviews, Ratings & Awards:
4-5 Logos underneath?

Target Market(s)

Coastal place where a Hurricane 🌀 🌀 Hits

Industry/Entity Type

Hurricane Public Insurance Adjuster

Font styles to use
Sans Serif
Other font styles liked:
• Calvera fonts

Colors
0054AA
0677BA
7BADD7
CADEEF
E8F1F8
EE7325
F08F49
F5BC92
FAE3D3
FDF4ED

Requirements
Must have
• Use my past project logos, colors, and schemes to create eye grabbing BillBoard
Nice to have
Should not have
• Not be too busy, must be Easy to Read, Eye Catchy

```html
<!DOCTYPE html>
<html lang="en">
<head>
<meta charset="utf-8">
<title>Hurricane Season Billboard – Claim Warden Group</title>
<link href="https://fonts.googleapis.com/css2?family=Poppins:wght@400;500;600;700;800&display=swap" rel="stylesheet">
<style>
  :root{
    --navy:#0a1a3a;
    --night:#06122a;
    --blue:#0677BA;
    --sky:#18a7e8;
    --orange:#F0890F;
    --white:#ffffff;
    --ink:#0b1b33;
    --red:#e0261b;
    --green:#6abf2c;
    --page:#f2f4f7;
  }
  *{margin:0;padding:0;box-sizing:border-box}
  html,body{width:999px;height:1200px;overflow:hidden;background:var(--page)}
  body{font-family:'Poppins',sans-serif;position:relative}

  .billboard{position:absolute;left:50px;top:469px;width:900px;height:262px;background:var(--white);overflow:hidden;box-shadow:0 4px 14px rgba(0,0,0,.12)}

  .storm-panel{position:absolute;left:0;top:0;width:469px;height:262px;
    background:radial-gradient(ellipse at 70% 50%,#1b3f7a 0%,#0c2550 40%,var(--night) 80%)}

  .headline{position:absolute;left:25px;top:24px;font-weight:800;font-size:34px;line-height:31px;letter-spacing:.3px;text-transform:uppercase}
  .headline .lead{color:var(--white)}
  .headline .hot{color:var(--orange)}
  .divider{position:absolute;left:25px;top:141px;width:112px;height:2px;background:var(--sky)}
  .tagline{position:absolute;left:25px;top:155px;color:var(--white);font-weight:400;font-size:18.5px;line-height:24px}
  .policyholder{position:absolute;left:25px;top:205px;color:var(--sky);font-weight:800;font-size:25px;letter-spacing:.3px}

  .brand-mark{position:absolute;left:392px;top:56px;width:148px;height:148px;border-radius:50%;background:var(--white);
    display:flex;align-items:center;justify-content:center;text-align:center;
    color:var(--blue);font-weight:800;font-size:20px;line-height:23px;z-index:3}

  .experience{position:absolute;left:563px;top:16px;display:flex;align-items:flex-start}
  .experience .num{color:var(--orange);font-weight:800;font-size:78px;line-height:70px;letter-spacing:-2px}
  .experience .plus{color:var(--orange);font-weight:800;font-size:36px;line-height:30px;margin-left:2px}
  .experience .years{position:absolute;left:108px;top:28px;color:var(--ink);font-weight:800;font-size:14px;line-height:14px;text-transform:uppercase}
  .vip-box{position:absolute;left:564px;top:89px;width:204px;height:31px;background:var(--blue);color:var(--white);
    font-weight:800;font-size:13px;line-height:13.5px;text-align:center;padding-top:2px;text-transform:uppercase}
  .award{position:absolute;left:783px;top:38px;width:80px;height:82px;border-radius:4px;
    background:linear-gradient(160deg,#9fb1c9,#2b4b8a 50%,#7b1d2a)}

  .call-band{position:absolute;left:500px;top:130px;width:400px;height:65px;background:var(--navy);
    clip-path:polygon(18% 0,100% 0,100% 100%,0 100%)}
  .call-text{position:absolute;left:560px;top:137px;width:340px;text-align:center;color:var(--white)}
  .call-text .phone{font-weight:800;font-size:18.5px;line-height:26px}
  .call-text .phone span{color:var(--sky)}
  .call-text .url{font-weight:700;font-size:14px;line-height:20px;letter-spacing:.6px}

  .reviews{position:absolute;left:515px;top:205px;width:380px;height:50px}
  .review{position:absolute;top:0;text-align:center}
  .zentrio{left:0;top:2px}
  .zentrio .name{color:var(--blue);font-weight:600;font-size:20px;line-height:22px}
  .stars{color:var(--orange);font-size:10px;letter-spacing:1px;line-height:12px}
  .qtr{left:90px}
  .qtr .badge{width:68px;height:24px;border-radius:3px;background:var(--blue);margin:0 auto}
  .qtr .rating{color:var(--navy);font-weight:700;font-size:6px;margin-top:2px}
  .aplus{left:168px}
  .aplus .title{color:var(--red);font-weight:600;font-size:15px;line-height:16px}
  .aplus .small{color:var(--ink);font-size:6.5px;line-height:7px}
  .aplus .source{color:var(--ink);font-size:4px;line-height:6px}
  .blocklink{left:282px;top:12px;color:var(--green);font-weight:700;font-size:16px}
</style>
</head>
<body>
  <section class="billboard" aria-label="Claim Warden Group hurricane season billboard">
    <div class="storm-panel" role="img" aria-label="Dark stormy night sky with blue lightning bolts"></div>

    <h1 class="headline">
      <span class="lead">Don't let the</span><br>
      <span class="hot">Hurricane</span><br>
      <span class="hot">Ruin your life!!</span>
    </h1>
    <div class="divider"></div>
    <p class="tagline">Your Best, Locally-Based<br>Private Adjuster &amp; Advocate</p>
    <p class="policyholder">FOR THE POLICYHOLDER!!</p>

    <div class="call-band"></div>

    <div class="brand-mark">Claim<br>Warden<br>Group</div>

    <div class="experience">
      <span class="num">20</span><span class="plus">+</span>
      <span class="years">Years of<br>Experience</span>
    </div>
    <div class="vip-box">Recovering millions<br>for our VIP clients</div>
    <div class="award" role="img" aria-label="Best of 2022 award plaque"></div>

    <div class="call-text">
      <div class="phone">CALL 850-555-0142 <span>GOT CLAIM?</span></div>
      <div class="url">www.theclaimwardengroup.com</div>
    </div>

    <div class="reviews">
      <div class="review zentrio"><div class="name">Zentrio</div><div class="stars">★★★★★</div></div>
      <div class="review qtr"><div class="badge"></div><div class="rating">QTR+ Rating: A+</div></div>
      <div class="review aplus">
        <div class="title">A+ Rating</div>
        <div class="small">Highest Rating For<br>Public Insurance Adjusters</div>
        <div class="source">(Source: ClaimScope)</div>
      </div>
      <div class="review blocklink">Blocklink</div>
    </div>
  </section>
</body>
</html>
```